Harborline Motors LLC

Car Dealer Customer Service
Address: 2741 Linden Avenue, Shelbyville, TN 37162
web: www.harborlinemotorstn.net
email: harborlinemotorstn@mailbox-example.net
Phone: (931) 555-0148
Phone: (629) 555-0173

```html
<!DOCTYPE html>
<html lang="en">
<head>
<meta charset="utf-8">
<title>Harborline Motors — Business Card</title>
<link rel="stylesheet" href="https://fonts.googleapis.com/css2?family=Poppins:wght@400;600;700&display=swap">
<style>
  :root {
    --backdrop: #d6d6d6;
    --card: #ffffff;
    --blue: #2690c8;
    --blue-deep: #1b75a8;
    --gold: #e9b143;
    --cream: #f6e6c8;
    --white: #ffffff;
  }
  * { margin: 0; padding: 0; box-sizing: border-box; }
  html, body {
    width: 1200px; height: 1200px; overflow: hidden;
    background: var(--backdrop);
    font-family: "Poppins", sans-serif;
  }
  .canvas { position: relative; width: 1200px; height: 1200px; }
  .card {
    position: absolute; left: 144px; width: 911px; height: 520px;
    background: var(--card); overflow: hidden;
  }
  .card--front { top: 59px; }
  .card--back { top: 620px; }

  .band { position: absolute; background: var(--blue); height: 56px; }
  .front-band-top {
    top: 0; left: 0; width: 466px;
    clip-path: polygon(0 0, 100% 0, 417px 100%, 0 100%);
  }
  .front-band-bottom {
    bottom: 0; right: 0; width: 469px;
    clip-path: polygon(51px 0, 100% 0, 100% 100%, 0 100%);
  }
  .vehicle-backdrop {
    position: absolute; left: 5px; top: 68px; width: 906px; height: 336px;
    background: radial-gradient(ellipse at 40% 45%, rgba(246,230,200,.75), rgba(246,230,200,.25) 60%, rgba(255,255,255,0) 80%);
  }
  .brand-mark {
    position: absolute; border-radius: 50%;
    background: linear-gradient(180deg, var(--blue), var(--blue-deep));
  }
  .front-mark { left: 355px; top: 104px; width: 210px; height: 210px; }
  .front-name {
    position: absolute; left: 0; right: 0; top: 338px;
    text-align: center; color: var(--blue-deep); white-space: nowrap;
    font-weight: 700; font-size: 44px; letter-spacing: 1px; line-height: 1;
  }

  .back-band-top {
    top: 0; right: 0; width: 460px;
    clip-path: polygon(0 0, 100% 0, 100% 100%, 51px 100%);
  }
  .back-mark { left: 84px; top: 56px; width: 206px; height: 206px; }
  .role {
    position: absolute; left: 331px; width: 540px; text-align: center;
    color: var(--gold); font-weight: 700; line-height: 1; white-space: nowrap;
  }
  .role__title { top: 126px; font-size: 66px; letter-spacing: 0; }
  .role__subtitle { top: 199px; font-size: 32px; font-weight: 700; letter-spacing: .3px; }

  .gold-rule { position: absolute; left: 0; right: 0; top: 301px; height: 11px; background: var(--gold); }
  .contact-panel { position: absolute; left: 0; right: 0; top: 312px; bottom: 0; background: var(--blue); }
  .name-tab {
    position: absolute; left: 0; bottom: 0; width: 463px; height: 56px; background: var(--card);
    clip-path: polygon(0 0, 413px 0, 100% 100%, 0 100%);
  }
  .name-tab__text {
    position: absolute; left: 48px; top: 12px; color: var(--blue); white-space: nowrap;
    font-weight: 700; font-size: 31px; letter-spacing: .5px; line-height: 1;
  }
  .phones { position: absolute; left: 76px; top: 340px; color: var(--white); font-size: 35px; line-height: 50px; white-space: nowrap; }
  .details {
    position: absolute; right: 52px; top: 347px; text-align: right; color: var(--white);
    font-size: 24px; line-height: 31px; white-space: nowrap;
  }
  .details__email, .details__web { font-size: 20px; line-height: 36px; }
  .details__email { margin-top: 6px; }
</style>
</head>
<body>
<div class="canvas">
  <section class="card card--front">
    <div class="vehicle-backdrop" role="img" aria-label="Faint illustration of a vintage car"></div>
    <div class="band front-band-top"></div>
    <div class="band front-band-bottom"></div>
    <div class="brand-mark front-mark"></div>
    <h1 class="front-name">HARBORLINE MOTORS</h1>
  </section>

  <section class="card card--back">
    <div class="band back-band-top"></div>
    <div class="brand-mark back-mark"></div>
    <p class="role role__title">CAR DEALER</p>
    <p class="role role__subtitle">CUSTOMER SERVICE</p>
    <div class="gold-rule"></div>
    <div class="contact-panel"></div>
    <div class="phones">
      <p>(931) 555-0148</p>
      <p>(629) 555-0173</p>
    </div>
    <div class="details">
      <p>2741 Linden Avenue,</p>
      <p>Shelbyville, TN 37162</p>
      <p class="details__email">harborlinemotorstn@mailbox-example.net</p>
      <p class="details__web">www.harborlinemotorstn.net</p>
    </div>
    <div class="name-tab"><span class="name-tab__text">HARBORLINE MOTORS</span></div>
  </section>
</div>
</body>
</html>
```